Twin Track Payout Duel Postcard creation

This is a mail marketing campaign that helps people create wealth while learning about this industry. I am looking to have a postcard designed that will have truthful information according to the flyers added. It needs to be clear that the potential amount of money any one can make is on the postcard somewhere. It also should get the point across that they dont need to sell and even if they cant get a referral they will be able to make money.
The "postcard attachment" is something I was working on and is an example of how to get the message across without putting all the detail in. I dont like what I have created which is why I am reaching out.

Target Market(s)

Mail Marketing Opportunity seekers

Industry/Entity Type

Font styles to use
Sans Serif
Decorative

Colors

Designer to choose colors to be used in the design.

Requirements
Must have
• My project must have a place for people to put a referring member name in. It also must have that the cost is $5 to get started. It must be clear that there are two income streams that people will qualify for when they join for $5. It must have the amount of money that can potentially be made in this program.
Nice to have
• A similar header to what you see on the attached flyer. as much info that can tactfully fit within a standard postcard. my email address for questions and my name and address for them to return the postcard and money to.
Should not have
• Misspellings

```html
<!DOCTYPE html>
<html lang="en">
<head>
<meta charset="utf-8">
<title>Twin Track Payout Duel Postcard</title>
<link href="https://fonts.googleapis.com/css2?family=Anton&family=Ubuntu:ital,wght@0,400;0,500;0,700;1,400;1,500&family=Cabin:wght@400;500;600&display=swap" rel="stylesheet">
<style>
  :root {
    --stage: #3b3b3d;
    --blue: #1b74c0;
    --sky: #bcd8ef;
    --grey-band: #58585a;
    --ink: #2b2b2b;
    --white: #ffffff;
  }
  * { box-sizing: border-box; margin: 0; padding: 0; }
  html, body { width: 800px; height: 1200px; overflow: hidden; }
  body { background: var(--stage); position: relative; font-family: "Ubuntu", sans-serif; }

  .card { position: absolute; left: 66px; width: 668px; height: 514px; background: var(--white); overflow: hidden; }
  .card--front { top: 69px; }
  .card--back { top: 616px; }

  /* Front */
  .truck { position: absolute; border-radius: 6px; }
  .truck--left { left: 38px; top: 35px; width: 108px; height: 92px;
    background: radial-gradient(circle at 50% 60%, #6a6a6a, #d8d8d8 70%, #fff 72%); }
  .truck--right { left: 514px; top: 23px; width: 132px; height: 104px;
    background: radial-gradient(circle at 50% 55%, #333, #9a9a9a 62%, #fff 70%); }

  .headline { position: absolute; left: 0; width: 668px; top: 42px; text-align: center;
    font-family: "Anton", sans-serif; font-size: 66px; line-height: 1; color: var(--blue); letter-spacing: 0.5px; }

  .sky-band { position: absolute; left: 0; top: 149px; width: 668px; height: 150px;
    background: linear-gradient(180deg, var(--sky) 0%, #e6f1fa 70%, var(--white) 100%); }
  .rule-top { position: absolute; left: 0; top: 149px; width: 668px; height: 4px; background: var(--blue); }
  .title-pill { position: absolute; left: 102px; top: 135px; width: 464px; height: 36px; border-radius: 18px;
    background: var(--blue); color: var(--white); font-weight: 700; font-size: 23px;
    display: flex; align-items: center; justify-content: center; }

  .photo { position: absolute; border-radius: 50%; }
  .photo--bag { left: 142px; top: 179px; width: 184px; height: 184px; border: 6px solid var(--blue);
    background: radial-gradient(circle at 45% 50%, #c8a062 0%, #e2c69a 35%, #fff 62%); }
  .photo--cash { left: -10px; top: 268px; width: 232px; height: 232px; border: 6px solid var(--grey-band);
    box-shadow: 0 0 0 5px var(--blue);
    background: linear-gradient(135deg, #dfe5d6 0%, #9fae8c 45%, #c9d2bd 70%, #8d9a7c 100%); }

  .price { position: absolute; left: 366px; top: 176px; font-family: "Anton", sans-serif; font-style: italic;
    font-size: 104px; line-height: 1; color: var(--blue); transform: skewX(-8deg); }
  .price-tag { position: absolute; left: 506px; top: 188px; font-family: "Anton", sans-serif;
    font-size: 42px; line-height: 0.98; color: var(--grey-band); transform: skewX(-10deg); }

  .streams { position: absolute; left: 326px; top: 291px; width: 342px; height: 48px; background: var(--grey-band);
    color: var(--white); font-style: italic; font-size: 15px; line-height: 19px; text-align: right;
    padding: 5px 30px 0 10px; }

  .steps { position: absolute; right: 30px; top: 350px; width: 420px; text-align: right;
    font-family: "Cabin", sans-serif; font-size: 16.5px; line-height: 20px; color: var(--blue); }

  .rule-bottom { position: absolute; left: 0; top: 453px; width: 668px; height: 2px; background: var(--blue); }
  .email-band { position: absolute; left: 0; bottom: 0; width: 668px; height: 58px; background: var(--blue);
    color: var(--white); font-weight: 700; font-size: 25px; display: flex; align-items: center;
    justify-content: flex-end; padding-right: 30px; }
  .email-band--center { justify-content: center; padding-right: 0; }

  /* Back */
  .levels { position: absolute; left: 0; top: 0; width: 366px; height: 448px; background: var(--blue);
    color: var(--white); padding: 34px 22px 0 22px; font-family: "Cabin", sans-serif; }
  .levels h2 { font-size: 17.5px; line-height: 20.5px; font-weight: 600; margin-bottom: 14px; }
  .levels p { font-size: 12.6px; line-height: 16.3px; text-align: justify; margin-bottom: 13px; }
  .levels strong { font-size: 14px; font-weight: 600; }
  .levels .promise { font-weight: 600; margin-bottom: 0; }

  .stamp { position: absolute; left: 540px; top: 36px; width: 90px; height: 100px; background: var(--blue); }
  .referrer { position: absolute; left: 404px; top: 262px; width: 226px; font-family: "Cabin", sans-serif;
    font-size: 12.5px; color: var(--ink); }
  .referrer-line { position: absolute; left: 404px; top: 296px; width: 226px; height: 1.5px; background: var(--ink); }
  .address-line { position: absolute; left: 404px; width: 226px; height: 1.5px; background: var(--ink); }
  .back-rule { position: absolute; left: 0; top: 452px; width: 668px; height: 2px; background: var(--blue); }
</style>
</head>
<body>

<section class="card card--front">
  <div class="sky-band"></div>
  <div class="rule-top"></div>
  <div class="truck truck--left" role="img" aria-label="Cartoon monster truck"></div>
  <div class="truck truck--right" role="img" aria-label="Sketched monster truck"></div>
  <h1 class="headline">Introducing</h1>
  <div class="title-pill">Twin Track Payout Duel</div>

  <div class="photo photo--bag" role="img" aria-label="Money bag with gold coins"></div>
  <div class="photo photo--cash" role="img" aria-label="Stacks of dollar bills"></div>

  <div class="price">$5</div>
  <div class="price-tag">to get<br>started.</div>

  <div class="streams">There are two income streams that people<br>will qualify for when they join for $5</div>

  <p class="steps">Start engine: Send $5 to the monitor Harold<br>Vance, 218 Larch Ave, Pinecrest, WI 53000.<br>To move into 1st gear of both Auto and Manual<br>tracks you will just need 4 people placed under you.</p>

  <div class="rule-bottom"></div>
  <div class="email-band">Email: twintrack5@example.com</div>
</section>

<section class="card card--back">
  <div class="levels">
    <h2>The 3 levels are called Neutral, 2 Wheel Drive, and 4 Wheel Drive and are outlined below:</h2>
    <p><strong>Neutral:</strong> $5 you are entered into Twin Track Payout Duel program and need 4 referrals to move into the 1st gear of both the Auto and Manual tracks.</p>
    <p><strong>2 Wheel Drive:</strong> $15; $5 enters you into Twin Track Payout Duel program; $10 enters you into the 1st gear of the Manual Track (TwinTen). You will receive 3 entries that will be eligible to go through the Auto Track. You will only need 2 referrals per entry to enter them into the Auto Track. After 6 referrals you will have 3 entries that are going through the Auto Track.</p>
    <p><strong>4 Wheel Drive:</strong> $25; $5 enters you into Twin Track Payout Duel program; $10 enters you into the 1st gear of the Manual Track (TwinTen); $10 enters one entry into the Auto Track. You will have 4 extra entries that will go through the Auto Track for a total of 5. Each entry will enter the Auto Track after 2 referrals per entry are placed below them.</p>
    <p class="promise">No selling needed. Even without a referral, spillover can earn you money. Potential earnings: up to $______ across both tracks.</p>
  </div>

  <div class="stamp"></div>
  <div class="referrer">Referring member name:</div>
  <div class="referrer-line"></div>
  <div class="address-line" style="top:330px"></div>
  <div class="address-line" style="top:369px"></div>
  <div class="address-line" style="top:408px"></div>

  <div class="back-rule"></div>
  <div class="email-band email-band--center">Email: twintrack5@example.com</div>
</section>

</body>
</html>
```